Killer Webpage Design

I currently have a self-hosted webpage through wordpress at www.vantrelmedia.com - the content is complete and I'm happy with this but I need it designed (no coding) to complete my requirements. I'm happy to take designs which are non-Wordpress if there is specific advantage in this.

My full branding logos are attached along with color files. My main aim is consistent branding across all areas (social media, business cards, emails, websites). I have the rest running but am not happy with the available default selections from Wordpress.

I would prefer to use the darker blue version of the logo as I feel this has more standout in online media, however I would appreciate submissions with both variants to help me choose.

With the homepage I will also want to see blog pages and category pages designed but this can come after I have selected a design to go with,

Sites that I like and are related to my business include the following:
http://www.plumora.com/au/accounting-software/
http://www.taskgriddle.com/home.aspx
https://brimtill.com/register
Updates

Apologies for the confusion - to clarify for designers I am looking for design only, no coding.

FYI - i have now uploaded business cards for an idea of the contemporary style of design completed so far.

Target Market(s)

small to medium business. Not systemised but looking for help and support.

Industry/Entity Type

Business

Requirements
Must have
• I'm looking for a minimalist professional page, with the ability to easily add new sections when required. I will also need a CMS to add blog posts on the go, with the same features that it currently has (comments, social logon etc)

```html
<!DOCTYPE html>
<html lang="en">
<head>
<meta charset="utf-8">
<title>Vantrel Media – Blog</title>
<link href="https://fonts.googleapis.com/css2?family=PT+Sans:wght@400;700&display=swap" rel="stylesheet">
<style>
:root{
  --navy:#0a2131;
  --navy-deep:#061823;
  --teal:#2cb4cc;
  --teal-dark:#1d93ab;
  --teal-text:#1d7a93;
  --blog-red:#a3262b;
  --orange:#c9561f;
  --page:#f3f3f3;
  --card:#ececec;
  --card-line:#dcdcdc;
  --text:#333;
  --footer:#343434;
  --footer-text:#d8d8d8;
}
*{margin:0;padding:0;box-sizing:border-box}
html,body{width:874px;height:1200px;overflow:hidden}
body{font-family:"PT Sans",Arial,sans-serif;color:var(--text);background:var(--page);position:relative}
.header{position:absolute;left:0;top:0;width:874px;height:87px;background:linear-gradient(180deg,var(--navy) 0%,var(--navy-deep) 100%)}
.brand{position:absolute;left:74px;top:26px;display:flex;align-items:center;gap:10px}
.brand-mark{width:30px;height:30px;border-radius:50%;background:var(--teal)}
.brand-name{font-size:24px;font-weight:700;color:#fff}
.search{position:absolute;left:587px;top:33px;width:154px;height:21px;background:#fff;font-size:10px;color:#666;padding:4px 12px}
.search svg{position:absolute;right:8px;top:4px}
.lang{position:absolute;left:747px;top:33px;width:62px;height:21px;background:#fff;font-size:10px;color:#666;padding:4px 0 0 8px;display:flex;gap:5px}
.lang .flag{width:11px;height:8px;background:#5a6ea8;margin-top:3px}
.lang svg{margin-left:6px;margin-top:4px}
.nav{position:absolute;left:0;top:87px;width:874px;height:39px;background:linear-gradient(180deg,#37c0d6,var(--teal));border-top:1px solid #5fd0e2}
.nav ul{list-style:none;display:flex;position:absolute;left:66px;top:0;height:39px}
.nav li{font-size:12px;color:#fff;padding:0 10.5px;line-height:38px;border-right:1px solid var(--teal-dark);text-shadow:0 1px 1px rgba(0,0,0,.25)}
.nav li.active{background:var(--teal-dark);padding:0 13px}
.hero{position:absolute;left:0;top:126px;width:874px;height:229px;background:linear-gradient(180deg,#4b7ea8 0%,#7ea5c4 55%,#d8e2ea 100%)}
.hero-visual{position:absolute;left:128px;top:14px;width:184px;height:215px;border-radius:90px 90px 6px 6px;background:radial-gradient(circle at 45% 40%,#e6f0f7,#8fb2cc 70%,#6f93b1)}
.hero-box{position:absolute;left:393px;top:32px;width:416px;height:171px;background:rgba(35,55,70,.72);padding:14px 29px}
.hero-box h1{font-size:18px;line-height:26px;font-weight:700;color:#fff}
.hero-box p{font-size:10.5px;line-height:17px;color:#fff;margin-top:8px}
.demo{position:absolute;left:29px;top:118px;width:122px;height:32px;background:#fff;border-radius:3px;font-size:15px;color:#333;padding:6px 9px;display:flex;align-items:center;gap:8px}
.demo b{font-weight:700}
.demo span.go{width:16px;height:16px;border-radius:50%;background:#666;display:flex;align-items:center;justify-content:center}
.blog-title{position:absolute;left:66px;top:372px;font-size:18px;font-weight:700;color:var(--blog-red)}
.post-visual{position:absolute;left:67px;top:412px;width:232px;height:130px;background:linear-gradient(90deg,#5a4a3c,#a28f72 55%,#d9c08a);border-radius:2px}
.post-head{position:absolute;left:321px;top:413px;width:232px}
.post-head h2{font-size:13.5px;line-height:17px;font-weight:400;color:var(--teal-text)}
.meta{font-size:9.5px;color:#333;margin-top:4px}
.excerpt{font-size:10px;line-height:16.8px;text-align:justify;margin-top:9px}
.post-body{position:absolute;left:67px;top:565px;width:486px;font-size:10px;line-height:16.8px;text-align:justify}
.post-body p{margin-bottom:6px}
.social{position:absolute;left:67px;top:987px;display:flex;gap:8px;font-size:8.5px}
.social .btn{border:1px solid #bbb;background:#f8f8f8;border-radius:2px;padding:1px 4px;display:flex;align-items:center;gap:3px;color:#2a4c8a}
.social .btn i{width:8px;height:8px;background:#3a5a9a;display:block}
.social .count{border:1px solid #bbb;background:#fff;padding:1px 4px;border-radius:2px;color:#333}
.pager{position:absolute;left:371px;top:1053px;display:flex;gap:3px;align-items:center}
.pager span{width:16px;height:16px;border-radius:2px;background:#cfcfcf;font-size:7.5px;color:#888;text-align:center;line-height:16px}
.pager span.current{background:#8c8c8c;color:#fff}
.pager em{font-style:normal;font-size:8px;color:#888;width:12px;text-align:center}
.side-title{position:absolute;left:602px;font-size:18px;font-weight:700;color:var(--orange)}
.card{position:absolute;left:602px;width:207px;height:101px;background:var(--card);border:1px solid var(--card-line);border-radius:2px}
.card .thumb{position:absolute;left:9px;top:10px;width:77px;height:80px}
.card .txt{position:absolute;left:96px;top:12px;width:102px;font-size:11.5px;line-height:16.8px;color:var(--teal-text);text-align:justify}
.card .date{position:absolute;left:96px;top:70px;font-size:9.5px;color:#333}
.footer{position:absolute;left:0;top:1118px;width:874px;height:82px;background:var(--footer)}
.footer ul{list-style:none;display:flex;position:absolute;left:66px;top:20px;font-size:10.5px;color:var(--footer-text)}
.footer li+li::before{content:"|";padding:0 10px}
.copy{position:absolute;left:66px;top:47px;font-size:10.5px;color:var(--footer-text)}
.social-icons{position:absolute;left:768px;top:32px;display:flex;gap:4px}
.social-icons span{width:18px;height:18px;border-radius:3px;background:#4c7cc4}
.social-icons span+span{background:#4cb6e6}
</style>
</head>
<body>
<header class="header">
  <div class="brand"><span class="brand-mark"></span><span class="brand-name">Vantrel Media</span></div>
  <div class="search">Search
    <svg width="12" height="12" viewBox="0 0 12 12"><circle cx="5" cy="5" r="3.5" fill="none" stroke="#333" stroke-width="1.8"/><path d="M7.5 7.5L11 11" stroke="#333" stroke-width="2"/></svg>
  </div>
  <div class="lang"><span class="flag"></span>Eng<svg width="8" height="5" viewBox="0 0 8 5"><path d="M0 0h8L4 5z" fill="#555"/></svg></div>
</header>
<nav class="nav">
  <ul>
    <li class="active">Home</li>
    <li>Software Training and Implementation</li>
    <li>Project Management</li>
    <li>Business Process Analysis</li>
    <li>Blog</li>
    <li>About Us</li>
    <li>Contact Us</li>
  </ul>
</nav>
<section class="hero">
  <div class="hero-visual" role="img" aria-label="Glass globe on a pedestal against a cloudy sky"></div>
  <div class="hero-box">
    <h1>Curabitur non massa vestibulum, egestas velit vitae, imperdiet velit.</h1>
    <p>Aliquam interdum sollicitudin odio. Mauris nunc ante, sagittis id porta quis, semper non neque. Suspendisse ac pulvinar tellus.</p>
    <div class="demo"><span><b>FREE</b> Demo</span><span class="go"><svg width="7" height="8" viewBox="0 0 7 8"><path d="M1 0l5 4-5 4" fill="none" stroke="#fff" stroke-width="1.6"/></svg></span></div>
  </div>
</section>
<main>
  <h2 class="blog-title">Blog</h2>
  <div class="post-visual" role="img" aria-label="Hands using a tablet computer"></div>
  <div class="post-head">
    <h2>Atullam volutpat dui et nisl pharetra, in convallis ipsum</h2>
    <div class="meta">July-31-13 &nbsp;:: &nbsp;10.15 a.m</div>
    <p class="excerpt">Pellentesque at tristique nunc. Nunc quam orci, egestas et tortor et, molestie adipiscing velit. Nunc hen drerit risus ut dui condimentum dignis-sim. Sed nec mattis augue.</p>
  </div>
  <article class="post-body">
    <p>Duis facilisis pulvinar orci luctus molestie. Duis eget arcu ut magna pulvinar sagittis. Praesent gravida, sapien id hendrerit porttitor, purus tellus sagittis sem, et sagittis eros dolor eu tellus. Sed vel mattis sem. Pellentesque habitant morbi tristique senectus et netus et malesuada fames ac turpis egestas. Mauris nec neque quis urna eleifend dictum. Class aptent taciti sociosqu ad litora torquent per conubia nostra, per inceptos himenaeos. Nam sagittis volutpat tellus, eu cursus libero sodales in. In commodo sed odio sed auctor. Vestibulum euismod velit vel sem consequat blandit. Maecenas tempus ut ante nec pharetra. Sus-pendisse sodales auctor dui, et pulvinar nulla dignissim facilisis. Vivamus a congue eros. Suspendisse potenti. Sed tincidunt quis elit posuere aliquet.</p>
    <p>Etiam accumsan magna ac molestie tempus. Nulla eu tincidunt velit, quis elementum sapien. Curabitur quis tempor massa. Praesent et nulla auctor, pellentesque magna vel, ornare tortor. Vivamus dui metus, semper vel tincidunt vel, adipiscing condimentum tellus. Nulla vestibulum fermentum lectus ac gravida. Maecenas in mollis erat. Pellentesque consectetur, felis quis blandit convallis, ipsum justo laoreet magna, sed pretium odio sem sit amet sapien. Nullam mollis accumsan fermentum. Cras ac tincidunt nulla. Sus-pendisse mollis auctor mi, vitae vestibulum dolor consectetur sit amet.</p>
    <p>Vivamus felis arcu, blandit ut sapien a, semper sodales nulla. Quisque purus turpis, commodo quis sem in, faucibus posuere metus. Fusce mattis euismod facilisis. Vestibulum tincidunt ligula at nibh consequat, vehicula varius massa feugiat. Mauris vel odio sed elit aliquam pharetra ut vel leo. Maecenas viverra quis nibh eget eleifend. Donec vel justo sit amet metus facilisis placera.</p>
    <p>Duis a auctor nisl. Suspendisse suscipit metus eget euismod varius. Fusce elit neque, fermentum et elit sit amet, consequat euismod eros. Duis turpis mi, sagittis mattis turpis vitae, cursus scelerisque metus. Donec laoreet, libero vel volutpat scelerisque, mauris quam cursus elit, quis scelerisque est neque in dolor. Etiam rhoncus congue venenatis. Etiam eros lorem, malesuada eu metus vel, sodales varius augue. Mauris viverra, massa sed placerat tempor, nunc lectus accumsan felis, et sollicitudin velit leo sed nibh.</p>
  </article>
  <div class="social">
    <span class="btn"><i></i>Like</span><span class="count">3k</span>
    <span class="btn"><i></i>Share</span><span class="count">316</span>
  </div>
  <div class="pager">
    <span class="current">1</span><span>2</span><span>3</span><span>4</span><span>5</span><span>6</span><span>7</span><span>8</span><span>»</span><em>…</em><span>»»</span>
  </div>
</main>
<aside>
  <h3 class="side-title" style="top:384px">Popular Post</h3>
  <div class="card" style="top:412px"><div class="thumb" role="img" aria-label="Blue cloud computing graphic" style="background:linear-gradient(160deg,#3fa8e8,#0c5fb8)"></div><p class="txt">Mauris aptet neque quis pretium eifend dictum</p><span class="date">July-31-13 &nbsp;:: &nbsp;10.15 a.m</span></div>
  <div class="card" style="top:516px"><div class="thumb" role="img" aria-label="White 3D figure reading in an armchair" style="background:linear-gradient(180deg,#fafafa,#d8d8d8)"></div><p class="txt">Mauris aptet neque quis pretium eifend dictum</p><span class="date">July-31-13 &nbsp;:: &nbsp;10.15 a.m</span></div>
  <div class="card" style="top:620px"><div class="thumb" role="img" aria-label="Businessman among office towers under a blue sky" style="background:linear-gradient(180deg,#6aa2d8,#c7dbee 60%,#3a4a5a)"></div><p class="txt">Mauris aptet neque quis pretium eifend dictum</p><span class="date">July-31-13 &nbsp;:: &nbsp;10.15 a.m</span></div>
  <h3 class="side-title" style="top:742px">Older Post</h3>
  <div class="card" style="top:769px"><div class="thumb" role="img" aria-label="Finger touching a blue screen" style="background:linear-gradient(135deg,#1c4f9a,#5f9ad8 55%,#d8a27c)"></div><p class="txt">Mauris aptet neque quis pretium eifend dictum</p><span class="date">July-31-13 &nbsp;:: &nbsp;10.15 a.m</span></div>
  <div class="card" style="top:873px"><div class="thumb" role="img" aria-label="Cloud with tablet and phone devices" style="background:radial-gradient(circle at 50% 50%,#9cc9ea,#ffffff 70%)"></div><p class="txt">Mauris aptet neque quis pretium eifend dictum</p><span class="date">July-31-13 &nbsp;:: &nbsp;10.15 a.m</span></div>
  <div class="card" style="top:977px"><div class="thumb" role="img" aria-label="Businessman pointing at a network of people icons" style="background:linear-gradient(135deg,#d6e8f2,#8fb8d2 60%,#2b3d52)"></div><p class="txt">Mauris aptet neque quis pretium eifend dictum</p><span class="date">July-31-13 &nbsp;:: &nbsp;10.15 a.m</span></div>
</aside>
<footer class="footer">
  <ul>
    <li>Home</li><li>Software Training and Implementation</li><li>Project Management</li><li>Business Process Analysis</li><li>Blog</li><li>About Us</li><li>Contact Us</li>
  </ul>
  <p class="copy">Copyright &nbsp;© &nbsp;2013 &nbsp;&nbsp;Vantrel Media. &nbsp;&nbsp;&nbsp;All rights reserved.</p>
  <div class="social-icons"><span></span><span></span></div>
</footer>
</body>
</html>
```